Stylish Business Card for Modern hair salon

I need a simple business card design using our salon logo and colours that are in the logo. We service clients of all ages but predominantly those in the 18 to 55 age range. We have a young staff and are looking to have a card that will present a modern and clean image that represents who we are. The card should be in black and white same as our logo. Minimal use of other colours is allowed.

Industry/Entity Type

Hair And Beauty

Contact Information for Business Card

The design should have the following information
salon name - TR Hair Studio
address - 2751 Birchfield Rd.E. Mississauga, ON L7P3K2
phone - 905 614-2870
website - trhairexample.ca
instagram - tr.hairstudio
twitter - @TR_HairStudio

Colors
000000
ffffff
474747

Requirements
Must have
• simple design, salon name, address, phone, website, instagram, twitter info
• Back of card should have the following:
• YOUR NEXT APPOINTMENT
• DATE
• TIME
Nice to have
• simple design, clear to see and read,
• predominantly black and white colour, minimal use of other colours is ok
Should not have
• many colours, various fonts

```html
<!DOCTYPE html>
<html lang="en">
<head>
<meta charset="utf-8">
<title>TR Hair Studio – Business Card</title>
<link rel="stylesheet" href="https://fonts.googleapis.com/css2?family=Jost:ital,wght@0,400;1,400&display=swap">
<style>
  :root {
    --black: #000000;
    --white: #ffffff;
    --grey: #474747;
    --rule: #c8c8c8;
    --frame: #b5b5b5;
  }
  * { margin: 0; padding: 0; box-sizing: border-box; }
  html, body {
    width: 1200px; height: 1200px; overflow: hidden;
    background: var(--white);
    font-family: "Jost", "Futura", sans-serif;
  }
  .canvas { position: relative; width: 1200px; height: 1200px; }
  .card { position: absolute; top: 250px; width: 400px; height: 700px; }
  .card--front { left: 160px; background: var(--black); color: var(--white); }
  .card--back { left: 640px; background: var(--white); color: var(--black); border: 1px solid var(--frame); }

  .brand-name {
    position: absolute; left: 0; top: 162px; width: 100%;
    text-align: center; font-size: 38px; font-weight: 400; letter-spacing: 1px;
  }

  .salon-title {
    position: absolute; left: 78px; top: 386px;
    font-size: 32px; font-weight: 400; line-height: 40px; white-space: nowrap;
  }
  .title-rule {
    position: absolute; left: 58px; right: 0; top: 432px;
    height: 2px; background: var(--grey);
  }
  .contact {
    position: absolute; left: 78px; top: 454px;
    font-size: 17.5px; line-height: 20px;
  }
  .contact p { margin: 0; white-space: nowrap; }
  .contact .gap { margin-top: 22px; }
  .contact .links { margin-top: 26px; line-height: 27px; }
  .contact em { font-style: italic; }

  .appointment { position: absolute; left: 66px; top: 376px; }
  .appointment .lead { font-size: 19px; letter-spacing: 0.3px; }
  .appointment .main { font-size: 32px; line-height: 1.1; letter-spacing: 0.5px; }

  .field { position: absolute; left: 66px; width: 274px; display: flex; align-items: flex-end; font-size: 20px; }
  .field--date { top: 484px; }
  .field--time { top: 556px; }
  .field span { width: 70px; }
  .field .blank { flex: 1; height: 1px; background: var(--rule); margin-bottom: 2px; }
</style>
</head>
<body>
<div class="canvas">
  <section class="card card--front">
    <div class="brand-name">TR Hair Studio</div>
    <h1 class="salon-title">TR Hair Studio</h1>
    <div class="title-rule"></div>
    <div class="contact">
      <p>2751 Birchfield Rd.E.</p>
      <p>Mississauga, ON L7P3K2</p>
      <p class="gap">905 614-2870</p>
      <div class="links">
        <p><em>website:</em> trhairexample.ca</p>
        <p><em>instagram:</em> tr.hairstudio</p>
        <p><em>twitter:</em> @TR_HairStudio</p>
      </div>
    </div>
  </section>

  <section class="card card--back">
    <div class="brand-name">TR Hair Studio</div>
    <div class="appointment">
      <div class="lead">YOUR NEXT</div>
      <div class="main">APPOINTMENT</div>
    </div>
    <div class="field field--date"><span>DATE:</span><div class="blank"></div></div>
    <div class="field field--time"><span>TIME:</span><div class="blank"></div></div>
  </section>
</div>
</body>
</html>
```